Odvetnik - Attorney at law
Sodni tolmač za angleški jezik - English language Court Interpreter
Simple
Marjan Lesk
Odvetnik - Attorney at law Sodni tolmač za angleški jezik - English Language Court Interpreter
Brinjeva ulica 41 6000 Koper Slovenija
info@marjanlesk.example
www.marjanlesk.example
I invite all designers under logo project Attorney Marjan Lesk to participate. Please inform all designers.

```html
<!DOCTYPE html>
<html lang="sl">
<head>
<meta charset="utf-8">
<title>Marjan Lesk – Odvetnik</title>
<link rel="stylesheet" href="https://fonts.googleapis.com/css2?family=Cinzel:wght@400&family=Cormorant+Garamond:ital@1&family=Arimo:wght@400&display=swap">
<style>
  :root {
    --page-bg: #e9e9ec;
    --card-bg: #48438a;
    --card-edge: #3d3878;
    --ink-light: #ffffff;
    --ink-soft: #dcdaf0;
    --accent: #f08a2c;
    --mark-faint: rgba(255, 255, 255, 0.12);
  }
  html, body {
    margin: 0;
    width: 1200px;
    height: 951px;
    overflow: hidden;
    background: var(--page-bg);
  }
  .business-card {
    position: absolute;
    left: 100px;
    top: 195px;
    width: 1000px;
    height: 560px;
    border-radius: 34px;
    background: linear-gradient(160deg, var(--card-bg) 0%, var(--card-edge) 100%);
    overflow: hidden;
    color: var(--ink-light);
  }
  .faint-mark {
    position: absolute;
    right: 40px;
    top: -30px;
  }
  .brand {
    position: absolute;
    left: 70px;
    top: 150px;
    display: flex;
    align-items: center;
    gap: 22px;
  }
  .brand-dot {
    width: 58px;
    height: 58px;
    border-radius: 50%;
    background: var(--accent);
    flex: none;
  }
  .brand-name {
    font-family: "Cinzel", serif;
    font-size: 62px;
    line-height: 1;
    letter-spacing: 2px;
    margin: 0;
    font-weight: 400;
  }
  .brand-role {
    font-family: "Cormorant Garamond", serif;
    font-style: italic;
    font-size: 25px;
    color: var(--ink-soft);
    margin: 8px 0 0 4px;
  }
  .contact {
    position: absolute;
    left: 250px;
    top: 318px;
    font-family: "Arimo", sans-serif;
    font-size: 21px;
    line-height: 1.42;
    color: var(--ink-light);
  }
  .contact p { margin: 0; }
  .contact .label { margin-right: 6px; }
  .contact .gap { margin-left: 18px; }
  .contact .online { color: var(--accent); }
  .divider {
    position: absolute;
    left: 0;
    right: 0;
    top: 468px;
    height: 1px;
    background: rgba(255, 255, 255, 0.18);
  }
  .interpreter-line {
    position: absolute;
    left: 70px;
    top: 492px;
    margin: 0;
    font-family: "Arimo", sans-serif;
    font-size: 17px;
    letter-spacing: 1px;
    text-transform: uppercase;
    color: var(--ink-light);
  }
</style>
</head>
<body>
  <section class="business-card">
    <svg class="faint-mark" width="260" height="300" viewBox="0 0 260 300" aria-hidden="true">
      <circle cx="130" cy="150" r="120" fill="var(--mark-faint)"/>
    </svg>

    <header class="brand">
      <span class="brand-dot"></span>
      <div>
        <h1 class="brand-name">MARJAN LESK</h1>
        <p class="brand-role">Odvetnik - Attorney at law</p>
      </div>
    </header>

    <address class="contact">
      <p>Brinjeva ulica 41, 6000 Koper, Slovenija</p>
      <p><span class="label">Ph.</span>+386 5 5550142<span class="gap label">Cell</span>+386 40555387<span class="gap label">Fax</span>+386 5 5550143</p>
      <p class="online">info@marjanlesk.example<span class="gap">www.marjanlesk.example</span></p>
    </address>

    <div class="divider"></div>
    <p class="interpreter-line">Sodni tolmač za angleški jezik • English language court interpreter</p>
  </section>
</body>
</html>
```